Need a email blast flyer made

I am looking for someone to assist in making a flyer for my company that will effectively bring buyers to my table. I am looking at haveing a call to a to action as well as show people through images what it is we do. We are a heat transfer company that specializes in anything that screen printed transfers can be put on. They are very cool and practical. You can check out our site here. www.velquosign.example I am looking for someone who gets marketing and can convey to our target audience what it is we do and can do for you. Alot of promotional suppliers (who will be getting this ad) need this technology to do Stock Numbers on jerseys; short run products, full color process, tote bags, mylon application, ploy applications, umbrellas. Think anything with a logo and material we provide the transfers that you use a heat press to transfer or glue to product. We are very large but need something captivating to take us to the next level. please come up with something clean catchy professional and cool. Samples are attached of a flyer I am looking for for the email blast

Industry/Entity Type

Marketing

```html
<!DOCTYPE html>
<html lang="en">
<head>
<meta charset="utf-8">
<title>Velquosign – Custom Heat Transfer Flyer</title>
<link href="https://fonts.googleapis.com/css2?family=Montserrat:wght@300;400;700&family=Arimo:wght@400;700&display=swap" rel="stylesheet">
<style>
  :root {
    --page-bg: #e4e4e4;
    --paper: #ffffff;
    --ink-dark: #222222;
    --headline: #4f4f4f;
    --footer: #454545;
    --red: #ec1c24;
    --orange: #f7931e;
    --green: #3db54a;
    --blue: #1a75bb;
    --purple: #7b3f98;
    --nav-green: #6cbf45;
    --nav-yellow: #f2c12e;
    --nav-orange: #f79420;
    --nav-deep: #f15a24;
    --ring: #f04e23;
    --white: #ffffff;
  }
  * { margin: 0; padding: 0; box-sizing: border-box; }
  html, body { width: 1200px; height: 1000px; overflow: hidden; background: var(--page-bg); }
  .canvas { position: relative; width: 1200px; height: 1000px; }

  .flyer {
    position: absolute; left: 342px; top: 102px; width: 600px; height: 801px;
    background: var(--paper); overflow: hidden;
    box-shadow: 4px 4px 6px rgba(0,0,0,.35);
    font-family: "Arimo", Arial, sans-serif;
  }

  .swatch-fan { position: absolute; left: 0; top: 0; width: 375px; height: 275px; }

  .category-list { list-style: none; }
  .category {
    position: absolute; right: 0; height: 30px; color: var(--white);
    font-size: 18px; line-height: 30px; text-align: center;
    border-radius: 6px 0 0 6px; z-index: 2;
  }
  .category--jerseys { top: 36px; width: 174px; background: var(--red); }
  .category--tshirts { top: 82px; width: 174px; background: var(--orange); }
  .category--jackets { top: 128px; width: 174px; background: var(--green); }
  .category--bags    { top: 176px; width: 208px; background: var(--blue); padding-right: 28px; }
  .category--etc     { top: 223px; width: 174px; background: var(--purple); }

  .headline {
    position: absolute; left: 40px; top: 300px; width: 280px; color: var(--headline);
    font-family: "Montserrat", Arial, sans-serif; font-weight: 700; line-height: 1; z-index: 2;
  }
  .headline__top { display: block; font-size: 31px; letter-spacing: 2px; }
  .headline__main { display: block; font-size: 45px; letter-spacing: 2.5px; margin-top: 4px; }

  .intro {
    position: absolute; left: 20px; width: 298px; top: 380px;
    text-align: right; font-size: 11px; line-height: 14px; color: var(--ink-dark);
    letter-spacing: .4px; z-index: 2;
  }

  .product-photo {
    position: absolute; left: 345px; top: 260px; width: 255px; height: 248px;
    border-radius: 40% 0 0 30%;
    background: radial-gradient(circle at 40% 30%, #f6f6f6 0 26%, transparent 27%),
                linear-gradient(160deg, #d9ecf3 0%, #f7c9d8 35%, #2c2c2c 60%, #b01c1c 100%);
  }

  .ring-deco {
    position: absolute; left: 8px; top: 440px; width: 280px; height: 240px;
    border-radius: 50%;
    background: radial-gradient(circle, rgba(82,180,224,.35) 0%, rgba(82,180,224,.12) 60%, transparent 72%);
  }
  .cooler-photo {
    position: absolute; left: 49px; top: 457px; width: 186px; height: 186px;
    border-radius: 50%; border: 3px solid var(--ring);
    background: linear-gradient(170deg, #c9ccd0 0%, #9fa4aa 40%, #2f9fd9 65%, #1f7fbf 100%);
  }

  .benefits { list-style: none; font-size: 14px; color: var(--ink-dark); letter-spacing: .6px; }
  .benefit { position: absolute; white-space: nowrap; }
  .benefit--custom { left: 319px; top: 556px; }
  .benefit--variety { left: 380px; top: 585px; }
  .benefit--speed { left: 341px; top: 613px; }

  .flower-deco {
    position: absolute; right: 0; top: 608px; width: 80px; height: 76px;
    border-radius: 50% 0 0 50%;
    background: radial-gradient(circle, rgba(248,167,39,.45) 0%, rgba(56,169,214,.3) 50%, transparent 72%);
  }

  .nav { position: absolute; left: 108px; top: 679px; width: 492px; height: 24px; }
  .nav__tab {
    position: absolute; top: 0; height: 24px; color: var(--white);
    font-size: 12.5px; font-weight: 700; line-height: 24px; text-align: center;
  }
  .nav__tab svg { position: absolute; inset: 0; width: 100%; height: 100%; }
  .nav__tab span { position: relative; }
  .nav__tab--home { left: 0; width: 108px; }
  .nav__tab--service { left: 97px; width: 108px; }
  .nav__tab--products { left: 194px; width: 108px; }
  .nav__tab--quote { left: 291px; width: 108px; }
  .nav__tab--contact { left: 388px; width: 104px; }

  .footer {
    position: absolute; left: 0; top: 703px; width: 600px; height: 98px;
    background: var(--footer); color: var(--white);
  }
  .brand { position: absolute; left: 38px; top: 12px; }
  .brand__name {
    font-family: "Montserrat", Arial, sans-serif; font-weight: 300;
    font-size: 42px; line-height: 44px; letter-spacing: -.5px;
  }
  .brand__tagline { font-size: 11.5px; margin-top: 8px; letter-spacing: .2px; }
  .cta { position: absolute; left: 340px; top: 20px; }
  .cta__lead { font-size: 15px; letter-spacing: .3px; }
  .cta__phone {
    font-family: "Montserrat", Arial, sans-serif; font-weight: 700;
    font-size: 30px; letter-spacing: 1.8px; margin-top: 4px; line-height: 1;
  }
</style>
</head>
<body>
<div class="canvas">
  <article class="flyer">
    <svg class="swatch-fan" viewBox="0 0 375 275" role="img" aria-label="Fanned colour swatch cards in rainbow tones with butterflies">
      <defs>
        <linearGradient id="fanTones" x1="0" y1="1" x2="1" y2="0">
          <stop offset="0" stop-color="#e6337a"/>
          <stop offset=".25" stop-color="#e8232a"/>
          <stop offset=".45" stop-color="#6a2c91"/>
          <stop offset=".6" stop-color="#2b8fd6"/>
          <stop offset=".8" stop-color="#f7b21a"/>
          <stop offset="1" stop-color="#dfff6e"/>
        </linearGradient>
      </defs>
      <path d="M0 0 H372 C 330 120 260 210 150 255 C 100 270 40 250 0 205 Z" fill="url(#fanTones)"/>
    </svg>

    <ul class="category-list">
      <li class="category category--jerseys">Jerseys</li>
      <li class="category category--tshirts">T-shirts</li>
      <li class="category category--jackets">Jackets</li>
      <li class="category category--bags">canvas bags</li>
      <li class="category category--etc">Etc</li>
    </ul>

    <div class="product-photo" role="img" aria-label="Printed products: white t-shirt with rooster print, black cap and black sports bag, with colourful floral circles"></div>

    <h1 class="headline">
      <span class="headline__top">COSTUM HEAT</span>
      <span class="headline__main">TRANSFER</span>
    </h1>
    <p class="intro">Velquosign supplies garment manufacturers<br>with superb heat transfer products for use in a<br>variety of applications.</p>

    <div class="ring-deco" role="img" aria-label="Decorative blue and green rings and dots"></div>
    <div class="cooler-photo" role="img" aria-label="Blue insulated cooler bag with printed team logo, holding drink cans"></div>

    <ul class="benefits">
      <li class="benefit benefit--custom">In-House Customization</li>
      <li class="benefit benefit--variety">Variety and Flexibility</li>
      <li class="benefit benefit--speed">Fast Turnaround</li>
    </ul>

    <div class="flower-deco" role="img" aria-label="Decorative colourful flower swirl"></div>

    <nav class="nav">
      <div class="nav__tab nav__tab--home"><svg viewBox="0 0 108 24" preserveAspectRatio="none"><polygon points="11,0 108,0 97,24 0,24" fill="var(--nav-green)"/></svg><span>Home</span></div>
      <div class="nav__tab nav__tab--service"><svg viewBox="0 0 108 24" preserveAspectRatio="none"><polygon points="11,0 108,0 97,24 0,24" fill="var(--nav-yellow)"/></svg><span>Service</span></div>
      <div class="nav__tab nav__tab--products"><svg viewBox="0 0 108 24" preserveAspectRatio="none"><polygon points="11,0 108,0 97,24 0,24" fill="var(--nav-orange)"/></svg><span>Products</span></div>
      <div class="nav__tab nav__tab--quote"><svg viewBox="0 0 108 24" preserveAspectRatio="none"><polygon points="11,0 108,0 97,24 0,24" fill="var(--nav-deep)"/></svg><span>Get Quote</span></div>
      <div class="nav__tab nav__tab--contact"><svg viewBox="0 0 104 24" preserveAspectRatio="none"><polygon points="11,0 104,0 104,24 0,24" fill="var(--red)"/></svg><span>Contact us</span></div>
    </nav>

    <footer class="footer">
      <div class="brand">
        <div class="brand__name">velquosign</div>
        <div class="brand__tagline">Specialists in Heat Applied Graphics</div>
      </div>
      <div class="cta">
        <div class="cta__lead">Call us today for a free quote!</div>
        <div class="cta__phone">555-210-0800</div>
      </div>
    </footer>
  </article>
</div>
</body>
</html>
```